依頼詳細
表面はカラー、裏面は白黒で申し込み用紙にしようと考えています。
魅力のあるツアーだと思いますので、読み手に伝わるよう作成をお願いします。
〈ツアーのポイント〉
・透き通った青い海、緑の山々、満天の星空など、大自然に囲まれたダイナミックな眺望
・貸切バスで観光スポットをご案内
・地元の食材にこだわった料理を堪能
・島人との交流
・自然の中でBBQ、キャンプファイヤー
・宿泊は汐見島唯一の温泉宿
・カップル成立で特典付き
・格安
など
多少変更が出るかもしれませんので、こちらでも編集できる形式で納品をお願いします。
ご不明点などありましたらご連絡ください。
よろしくお願いいたします。
記載項目
表現など変更して頂いて結構です。

【表面】
独身女性参加者募集
〈イベント名称〉渚トーク星結び
〈日時〉2015年7月3日(金)~2015年7月5日(日)
〈会場〉汐見島
〈ツアースケジュール〉
1日目 20:00 東京 灯波客船ターミナル集合(女性のみ)・女子会
23:00 出航(大型客船)
2日目 9:00 汐見島着・チェックイン
朝 男性合流・アイスブレイク
昼 昼食・島内観光
夜 BBQ・キャンプファイヤー・温泉旅館宿泊
3日目 朝 自由時間
13:35 汐見島発
17:30 東京 灯波客船ターミナル着・解散
〈ツアーのポイント〉依頼詳細参考
〈集合場所〉白浪航路灯波港 1階ロビー ※若葉環状線蓮見坂駅から徒歩8分
〈集合時間〉2015年7月3日(金)20:00
〈参加対象〉20歳~35歳の島外在住独身女性
〈募集人数〉15名(先着順)
〈参加料金〉15,000円/1人(交通費・宿泊費・食費込み)
〈申込方法〉裏面の申込書にご記入の上、メール・FAX・郵送にてお申込みください。
〈申込締切〉2015年6月7日(日)
〈ホームページ〉
※ホームページのURLを載せたいのですが、まだ出来上がっていないので後ほどURLを追加できるようにしていただきたいです。

裏面は補足情報に記載します。
サイズ
A4
ページ数
両面
希望イメージ
• +5 0 +5
• シンプル
複雑
• 単色
カラフル
• 暗い
明るい
• 日常
高級
• 遊び心
厳粛
• 未来的
伝統的
• 女性的
男性的
希望する色
赤系、水色系、緑系、黄・オレンジ系
納品ファイル
補足説明
【裏面】申込用紙
〈イベント名称〉
〈日時〉
〈会場〉
〈募集人数〉15名(先着順)
〈参加資格〉20歳から35歳までの汐見島外在住の独身女性
お一人様参加・シングルマザー・結婚歴あり歓迎
〈参加料金〉
MAIL  shiomi@hx.nagisanet-example.jp
メールでのお申し込みは①氏名②生年月日③住所④電話番号⑤メールアドレスを添えて上記のアドレスまでご送信ください。
FAX 04992-7-5530
〈申し込みフォーム〉
・氏名(ふりがな)
・氏名
・生年月日
・電話番号
・メールアドレス
・自己PR
〈注意事項〉
1 申し込み・キャンセルは6月7日(日)までにお願いします。
2 男女比は出来る限り調整しますが同数にならないこともありますのでご了承願います。
3 個人情報は厳重に管理し、本事業のみの使用とさせていただきます。
4 悪天候時はプログラム内容を変更または中止する場合があります。

申し込み受付後、事務局より順次詳細をお送りいたします。

問い合わせ・お申込み 汐見村商工会青年部事務局
〒100-0999 東京都汐見村汐見村2483番地
TEL  04992-7-4418
FAX  04992-7-5530

依頼公開後の追記内容
写真を添付します。

ターゲット層を対象にアンケート調査を実施した結果、最も多く票が集まったため。

この度は私どもの為に、多数ご提案をご用意していただき、誠にありがとうございます。どの提案も魅力を感じていましたが、上記の理由から一社選ばせていただきました。
折角親身にお世話をしていただいたところ、心苦しい限りですが、ご理解いただければ幸いです。
また、同様の機会があればよろしくお願いいたします。

```html
<!DOCTYPE html>
<html lang="ja">
<head>
<meta charset="utf-8">
<title>渚トーク星結び 参加申込書</title>
<link rel="stylesheet" href="https://fonts.googleapis.com/css2?family=Noto+Sans+JP:wght@400;500;700;900&family=M+PLUS+Rounded+1c:wght@700;800&display=swap">
<style>
  :root{
    --ink:#1a1a1a;
    --accent:#e2333b;
    --pink:#f6c9cf;
    --pink-deep:#e86d84;
    --yellow:#f3d23a;
    --rule:#333;
    --paper:#ffffff;
    --grey:#f0f0f0;
  }
  *{box-sizing:border-box;margin:0;padding:0}
  html,body{width:842px;height:1200px;overflow:hidden;background:var(--paper)}
  body{font-family:"Noto Sans JP",sans-serif;color:var(--ink);position:relative}
  .sheet{position:absolute;inset:0;padding:34px 46px 0}

  /* header */
  .header{position:relative;height:118px;text-align:center}
  .header .catch{font-family:"M PLUS Rounded 1c",sans-serif;font-weight:800;color:var(--accent);font-size:22px;letter-spacing:2px;position:absolute;left:300px;top:0}
  .header .title{font-weight:900;font-size:66px;letter-spacing:2px;line-height:1;position:absolute;left:50px;top:22px}
  .header .title small{font-size:46px;margin:0 6px}
  .badge{position:absolute;border-radius:50%;display:flex;align-items:center;justify-content:center;text-align:center;font-weight:700;line-height:1.15}
  .badge.stay{left:252px;top:0;width:46px;height:46px;background:var(--yellow);font-size:10px}
  .badge.plan{right:6px;top:2px;width:60px;height:60px;border:2px solid var(--pink-deep);color:var(--pink-deep);font-size:11px}
  .header .dates{position:absolute;left:300px;top:88px;font-weight:900;font-size:22px}
  .header .dates small{font-size:14px}

  /* info */
  .info{position:relative;height:150px;font-size:13px;line-height:1.75}
  .info dl{display:grid;grid-template-columns:84px 1fr;width:560px}
  .info dt{font-weight:700}
  .welcome{position:absolute;right:6px;top:60px;width:172px;padding:10px 8px;border-radius:10px;background:var(--pink);text-align:center;font-weight:700;font-size:12.5px;line-height:1.5}

  /* methods */
  .how{display:flex;align-items:center;gap:14px;height:34px;border-top:2px solid var(--rule);padding-top:6px;font-size:13px}
  .how .label{background:var(--ink);color:#fff;font-weight:700;padding:3px 12px;font-size:13px}
  .method{display:flex;align-items:center;gap:18px;height:66px;border-bottom:1px dotted #888}
  .method .tag{width:96px;height:54px;border:2px solid var(--ink);border-radius:6px;display:flex;flex-direction:column;align-items:center;justify-content:center;font-size:10px;font-weight:700}
  .method .value{font-weight:900;font-size:26px;letter-spacing:.5px}
  .method .value.mail{font-size:22px}
  .method .note{font-size:10.5px;line-height:1.5}
  .method .post{font-size:13px;font-weight:700;line-height:1.5}
  .after{font-size:12.5px;font-weight:700;text-align:center;margin:10px 0 8px}
  .cutline{border-top:2px dashed #666;margin:0 -46px}

  /* form */
  .form-title{font-weight:900;font-size:24px;text-align:center;margin:16px 0 10px}
  .form{width:100%;border-collapse:collapse;font-size:12px}
  .form th,.form td{border:1px solid var(--rule);padding:4px 8px;vertical-align:middle}
  .form th{background:var(--grey);width:110px;font-weight:700;text-align:center}
  .form .sm{font-size:10px;color:#444}
  .form .right{text-align:right}

  /* footer */
  .footer{display:flex;gap:14px;margin-top:14px;height:150px}
  .notes{flex:1;font-size:9.5px;line-height:1.6}
  .notes h3{font-size:10.5px;margin-bottom:2px}
  .notes ol{padding-left:14px}
  .contact{display:flex;width:330px;border:2px solid var(--ink)}
  .contact .vlabel{width:30px;background:var(--ink);color:#fff;writing-mode:vertical-rl;font-weight:700;font-size:12px;display:flex;align-items:center;justify-content:center}
  .contact .body{padding:10px 12px;font-size:11px;line-height:1.6}
  .contact .body strong{font-size:15px;font-weight:900;display:block;margin-bottom:4px}
</style>
</head>
<body>
<div class="sheet">
  <header class="header">
    <div class="badge stay">2泊<br>3日</div>
    <p class="catch">独身女性参加者募集!</p>
    <h1 class="title">渚トーク星結び</h1>
    <div class="badge plan">2泊3日<br>プラン</div>
    <p class="dates">2015年7月3日<small>(金)</small>～7月5日<small>(日)</small></p>
  </header>

  <section class="info">
    <dl>
      <dt>〈会　場〉</dt><dd>東京都 灯波客船ターミナル 1階ロビー（※若葉環状線蓮見坂駅から徒歩8分）／20:00集合<br>※白浪航路灯波港から大型客船で23:00出航</dd>
      <dt>〈募集人数〉</dt><dd>15名（先着順）</dd>
      <dt>〈参加資格〉</dt><dd>20歳から35歳までの汐見島外在住の独身女性</dd>
      <dt>〈参加料金〉</dt><dd>15,000円／1人（交通費・宿泊費・食費込み）</dd>
    </dl>
    <p class="welcome">お一人様参加・シングルマザー<br>結婚歴あり歓迎</p>
  </section>

  <div class="how"><span class="label">お申込方法</span><span>下記申込書を記入の上、メール・FAX・郵送にてお申込みください。</span></div>

  <div class="method">
    <div class="tag">
      <svg width="30" height="20" viewBox="0 0 30 20" aria-hidden="true"><rect x="1" y="1" width="28" height="18" fill="none" stroke="#1a1a1a" stroke-width="2"/><path d="M1 1 L15 11 L29 1" fill="none" stroke="#1a1a1a" stroke-width="2"/></svg>
      Mailでお申込み
    </div>
    <div>
      <p class="value mail">shiomi@hx.nagisanet-example.jp</p>
      <p class="note">メールでのお申込みは①氏名②生年月日③住所④電話番号⑤メールアドレスを添えて上記のアドレスまでご送信ください。</p>
    </div>
  </div>

  <div class="method">
    <div class="tag">
      <svg width="30" height="22" viewBox="0 0 30 22" aria-hidden="true"><rect x="7" y="1" width="16" height="8" fill="none" stroke="#1a1a1a" stroke-width="2"/><rect x="1" y="8" width="28" height="13" rx="2" fill="none" stroke="#1a1a1a" stroke-width="2"/><circle cx="23" cy="14" r="2" fill="#1a1a1a"/></svg>
      FAXでお申込み
    </div>
    <div>
      <p class="value">04992-7-5530</p>
      <p class="note">「参加申込書」をご記入の上、上記FAX番号までご送信ください。</p>
    </div>
  </div>

  <div class="method">
    <div class="tag">
      <svg width="24" height="22" viewBox="0 0 24 22" aria-hidden="true"><rect x="1" y="1" width="22" height="20" rx="2" fill="none" stroke="#1a1a1a" stroke-width="2"/><path d="M6 6 H18 M6 10 H18 M12 10 V18" stroke="#1a1a1a" stroke-width="2"/></svg>
      郵送でお申込み
    </div>
    <p class="post">「汐見村商工会青年部事務局」宛<br>〒100-0999 東京都汐見村汐見村2483番地</p>
  </div>

  <p class="after">※申し込み受付後、事務局より順次詳細をお送りいたします。</p>
  <div class="cutline"></div>

  <h2 class="form-title">渚トーク星結び「参加申込書」</h2>
  <table class="form">
    <tr style="height:26px"><th>フリガナ</th><td></td><th rowspan="2" style="width:70px">生年月日</th><td rowspan="2" class="right" style="width:170px">年　　月　　日</td><th rowspan="2" style="width:50px">年齢</th><td rowspan="2" class="right" style="width:60px">歳</td></tr>
    <tr style="height:44px"><th>氏　名</th><td></td></tr>
    <tr style="height:70px"><th>ご連絡先</th><td colspan="5" style="vertical-align:top">〒　　　　－<br><br><span class="sm">TEL（携帯電話でも可）</span></td></tr>
    <tr style="height:34px"><th>メールアドレス</th><td colspan="5"></td></tr>
    <tr style="height:96px"><th>自己PR</th><td colspan="5"></td></tr>
  </table>

  <footer class="footer">
    <div class="notes">
      <h3>〈注意事項〉</h3>
      <ol>
        <li>申し込み・キャンセルは6月7日(日)までにお願いします。</li>
        <li>男女比は出来る限り調整しますが同数にならないこともありますのでご了承願います。</li>
        <li>個人情報は厳重に管理し、本事業のみの使用とさせていただきます。</li>
        <li>悪天候時はプログラム内容を変更または中止する場合があります。</li>
      </ol>
    </div>
    <div class="contact">
      <div class="vlabel">お問い合わせ・お申込み</div>
      <div class="body">
        <strong>汐見村商工会青年部事務局</strong>
        〒100-0999 東京都汐見村汐見村2483番地<br>
        TEL 04992-7-4418　FAX 04992-7-5530<br>
        MAIL shiomi@hx.nagisanet-example.jp
      </div>
    </div>
  </footer>
</div>
</body>
</html>
```